Veltora Software Business Card Design

We are a new organization called Veltora. We are a software as a service provider. We deliver a project and program management solution via the internet, so everyone has the ability to work together and collaborate. Its an enterprise platform and we will focus on 50 plus employee company.

We have a website in place
www.veltora-demo.com

Use this as a start of producing the business card. The logo is there as well, but if you have a great and better solution...

Color scheme's could be inline with the website, but don't pin point on it. We can always change the website, logo, color scheme etc.

Target Market(s)

B2B, Projectmembers, projectmanagers, ICT, CTO, Marketing Managers

Industry/Entity Type

Software

Requirements
Must have
• Marten Kuyvelsma

Tel: +31 255 47 09 36
Mob: +31 6 927 15 062
marten@veltora-demo.com
Oostelingpad 84c
2184 KT Haarloord

Www.veltora-demo.com
social media links

```html
<!DOCTYPE html>
<html lang="en">
<head>
<meta charset="utf-8">
<title>Veltora Business Card</title>
<link href="https://fonts.googleapis.com/css2?family=Questrial&display=swap" rel="stylesheet">
<style>
  :root {
    --stage: #e6e7e2;
    --card: #ffffff;
    --brand-green: #8fa31a;
    --band-grey: #cfcfcf;
    --ink: #5a5a5a;
    --logo-ink: #ffffff;
  }
  * { margin: 0; padding: 0; box-sizing: border-box; }
  html, body {
    width: 1200px; height: 800px; overflow: hidden;
    background: var(--stage);
    font-family: "Questrial", "Century Gothic", sans-serif;
  }
  .business-card {
    position: absolute; left: 75px; top: 100px;
    width: 1050px; height: 600px;
    background: var(--card);
    box-shadow: 0 10px 30px rgba(0,0,0,0.18);
  }
  .brand-band {
    position: absolute; left: 0; top: 205px;
    width: 545px; height: 115px;
    background: var(--brand-green);
    display: flex; align-items: center;
    padding-left: 75px;
  }
  .brand-name {
    color: var(--logo-ink);
    font-size: 92px; line-height: 1;
    letter-spacing: 1px;
  }
  .accent-band {
    position: absolute; left: 0; top: 320px;
    width: 545px; height: 42px;
    background: var(--band-grey);
  }
  .divider {
    position: absolute; left: 568px; top: 105px;
    width: 3px; height: 440px;
    background: var(--brand-green);
  }
  .contact-block {
    position: absolute; left: 600px; top: 55px;
    color: var(--ink);
  }
  .person-name {
    font-size: 34px; letter-spacing: 1.5px;
    text-transform: uppercase;
    font-weight: 400;
    margin-bottom: 30px;
  }
  .contact-list { list-style: none; padding-left: 18px; }
  .contact-item {
    display: flex; align-items: center; gap: 14px;
    font-size: 26px; height: 43px;
  }
  .contact-icon { width: 28px; height: 28px; flex: none; }
  .contact-icon circle.ring { fill: none; stroke: var(--brand-green); stroke-width: 2; }
  .contact-icon .glyph { fill: var(--brand-green); stroke: none; }
  .contact-icon .line { fill: none; stroke: var(--brand-green); stroke-width: 1.6; }
  .address {
    font-style: normal;
    font-size: 26px; line-height: 1.3;
    margin-top: 28px; padding-left: 60px;
  }
</style>
</head>
<body>
  <div class="business-card">
    <div class="brand-band"><span class="brand-name">Veltora</span></div>
    <div class="accent-band"></div>
    <div class="divider"></div>

    <div class="contact-block">
      <h1 class="person-name">Marten Kuyvelsma</h1>
      <ul class="contact-list">
        <li class="contact-item">
          <svg class="contact-icon" viewBox="0 0 28 28" aria-hidden="true">
            <circle class="ring" cx="14" cy="14" r="12.5"/>
            <rect class="line" x="10" y="7" width="8" height="14" rx="1.5"/>
            <circle class="glyph" cx="14" cy="18.5" r="1"/>
          </svg>
          <span>+31 6 927 15 062</span>
        </li>
        <li class="contact-item">
          <svg class="contact-icon" viewBox="0 0 28 28" aria-hidden="true">
            <circle class="ring" cx="14" cy="14" r="12.5"/>
            <path class="glyph" d="M9.5 7.5l3 0 1.2 3.5-1.8 1.3c.9 1.8 2.3 3.2 4 4l1.3-1.8 3.5 1.2v3c0 .8-.7 1.4-1.5 1.3C12.6 19.5 8.5 15.4 8.2 9c0-.8.5-1.5 1.3-1.5z"/>
          </svg>
          <span>+31 255 47 09 36</span>
        </li>
        <li class="contact-item">
          <svg class="contact-icon" viewBox="0 0 28 28" aria-hidden="true">
            <circle class="ring" cx="14" cy="14" r="12.5"/>
            <rect class="glyph" x="7.5" y="9.5" width="13" height="9" rx="1"/>
            <path d="M8 10l6 5 6-5" fill="none" stroke="#fff" stroke-width="1.4"/>
          </svg>
          <span>marten@veltora-demo.com</span>
        </li>
        <li class="contact-item">
          <svg class="contact-icon" viewBox="0 0 28 28" aria-hidden="true">
            <circle class="ring" cx="14" cy="14" r="12.5"/>
            <circle class="line" cx="14" cy="14" r="7"/>
            <ellipse class="line" cx="14" cy="14" rx="3" ry="7"/>
            <path class="line" d="M7 14h14M8.5 10.5h11M8.5 17.5h11"/>
          </svg>
          <span>www.veltora-demo.com</span>
        </li>
        <li class="contact-item">
          <svg class="contact-icon" viewBox="0 0 28 28" aria-hidden="true">
            <circle class="ring" cx="14" cy="14" r="12.5"/>
          </svg>
          <span>/VeltoraCOM</span>
        </li>
        <li class="contact-item">
          <svg class="contact-icon" viewBox="0 0 28 28" aria-hidden="true">
            <circle class="ring" cx="14" cy="14" r="12.5"/>
          </svg>
          <span>/Veltora</span>
        </li>
      </ul>
      <address class="address">Oostelingpad 84c<br>2184 KT Haarloord</address>
    </div>
  </div>
</body>
</html>
```